Pathways to Brightmoor Land Ventures

size of the ad - 8”x 10.75" plus 0.25" bleed
I would like an ad for a magazine that will stand out and make people want to read the ad.
The ad should not be crowded and people reading the ad will be able to read the text.
I would like it to be a creative and modern-day design.
the list of topics should not be the focus of the ad.
the text is attached.
If you decide to use people in the ad then please no ladies.
please note that leave over 1 inch for the bottom of the footer

```html
<!DOCTYPE html>
<html lang="en">
<head>
<meta charset="utf-8">
<title>Real Estate Course – Pathways to Brightmoor Land Ventures</title>
<link rel="stylesheet" href="https://fonts.googleapis.com/css2?family=Barlow+Condensed:wght@300;400;500;600&family=Barlow:wght@400&family=Montserrat:wght@700&display=swap">
<style>
  :root {
    --orange: #f7941d;
    --white: #ffffff;
    --panel-top: rgba(18, 132, 185, 0.92);
    --panel-bottom: rgba(8, 84, 138, 0.94);
    --band-top: #1693bd;
    --band-bottom: #0a4b7a;
    --sky-top: #7f9dc2;
    --sky-mid: #c3cfdf;
    --house: #6d6f6f;
    --ground: #262a29;
  }
  * { margin: 0; padding: 0; box-sizing: border-box; }
  html, body { width: 927px; height: 1200px; overflow: hidden; background: var(--ground); }
  .ad {
    position: relative;
    width: 927px;
    height: 1200px;
    overflow: hidden;
    font-family: "Barlow Condensed", sans-serif;
  }
  .hero-photo {
    position: absolute; inset: 0;
    background: linear-gradient(180deg,
      var(--sky-top) 0%, var(--sky-mid) 30%, #b9bcc0 45%,
      var(--house) 62%, #4c4a44 80%, var(--ground) 100%);
  }
  .shapes { position: absolute; inset: 0; }
  .txt { position: absolute; left: 133px; text-transform: uppercase; }
  .course-title {
    top: 122px; color: var(--orange);
    font-weight: 600; font-size: 56px; line-height: 49px;
  }
  .course-subtitle {
    top: 294px; color: var(--white);
    font-weight: 500; font-size: 30px; line-height: 31px;
  }
  .tagline {
    left: 129px; top: 420px; color: var(--orange);
    font-weight: 300; font-size: 28px; line-height: 30px;
  }
  .location, .offer {
    left: 134px; color: var(--orange);
    font-family: "Montserrat", sans-serif; font-weight: 700; font-size: 25px;
    letter-spacing: 0.5px;
  }
  .location { top: 518px; }
  .offer { top: 650px; }
  .details {
    left: 134px; top: 558px; color: var(--white);
    font-weight: 400; font-size: 16.5px; line-height: 21px;
  }
  .offer-note {
    left: 134px; top: 688px; color: var(--white);
    font-weight: 400; font-size: 16.5px;
  }
  .topic-list {
    position: absolute; top: 926px; list-style: none;
    font-family: "Barlow", sans-serif; font-size: 14.5px; line-height: 18.2px;
    color: var(--white); text-transform: uppercase; letter-spacing: 0.3px;
  }
  .topic-list li::before { content: "▪"; font-size: 9px; margin: 0 8px 0 -13px; vertical-align: 2px; }
  .topic-list.first { left: 247px; }
  .topic-list.second { left: 619px; }
</style>
</head>
<body>
<div class="ad">
  <div class="hero-photo" role="img" aria-label="Photo of a modern house with wood and shingle siding at dusk, lit windows, under a pale evening sky"></div>

  <svg class="shapes" width="927" height="1200" viewBox="0 0 927 1200" aria-hidden="true">
    <defs>
      <linearGradient id="panelFill" x1="0" y1="0" x2="1" y2="1">
        <stop offset="0" stop-color="var(--panel-top)"/>
        <stop offset="1" stop-color="var(--panel-bottom)"/>
      </linearGradient>
      <linearGradient id="bandFill" x1="0" y1="0" x2="0" y2="1">
        <stop offset="0" stop-color="var(--band-top)"/>
        <stop offset="1" stop-color="var(--band-bottom)"/>
      </linearGradient>
    </defs>
    <polygon points="96,92 572,92 572,760 411,760 332,841 251,760 96,760" fill="url(#panelFill)"/>
    <polygon points="0,824 251,824 329,907 411,824 927,824 927,1055 0,1055" fill="url(#bandFill)"/>
    <text transform="translate(173,1022) rotate(-90)" textLength="168" lengthAdjust="spacingAndGlyphs"
          font-family="Montserrat, sans-serif" font-weight="700" font-size="44"
          fill="none" stroke="#ffffff" stroke-width="1.3">TOPICS</text>
    <text transform="translate(190,1015) rotate(-90)" textLength="160" lengthAdjust="spacingAndGlyphs"
          font-family="Montserrat, sans-serif" font-weight="700" font-size="16"
          fill="#f7941d">PARTIAL LISTING</text>
  </svg>

  <h1 class="txt course-title">Real<br>Estate<br>Course</h1>
  <h2 class="txt course-subtitle">Pathways to<br>Brightmoor Land<br>Ventures</h2>
  <p class="txt tagline">Investing in knowledge is<br>investing in opportunities.</p>
  <p class="txt location">Kestrel Hill</p>
  <p class="txt details">10 -Tuesday evenings sessions<br>Starting Feb.28<br>Limited partial scholarships</p>
  <p class="txt offer">Early Bird Special</p>
  <p class="txt offer-note">For those that started or would like to go into real estate</p>

  <ul class="topic-list first">
    <li>Real estate investment strategies</li>
    <li>Due diligence</li>
    <li>Financing</li>
    <li>Underwriting</li>
    <li>Property management</li>
  </ul>
  <ul class="topic-list second">
    <li>Real estate legal basics</li>
    <li>Sourcing deals</li>
    <li>Syndication</li>
    <li>Dealing with brokers</li>
    <li>Tax fundamentals</li>
  </ul>
</div>
</body>
</html>
```